Plimbo.com re-design on Wix platform

Re-do this website : www.plimbo.com
Plimbo is a sound conditioner that uses the calming, sedative qualities of mundane rhythmic stimulation to allow its users to rest easier and deeper than they normally would.
I think of Plimbo.com as a web app; a place to use and buy the product. Im open to suggestion on site layouts, whether you use one page or several.
Use the same color scheme: purple, white, black, grey/silver
I would like a place for testimonials, even though you don't currently see one on the site. Other than that, assume the content will stay mostly the same.
I'd like a clean, modern, professional look. The site will reside on Wix platform.

```html
<!DOCTYPE html>
<html lang="en">
<head>
<meta charset="utf-8">
<title>Plimbo – Sleep deeper</title>
<link rel="stylesheet" href="https://fonts.googleapis.com/css2?family=EB+Garamond:wght@400;500&family=Mulish:wght@300;400;600&display=swap">
<style>
  :root {
    --purple: #9d0a9f;
    --white: #ffffff;
    --black: #1a1a1a;
    --text: #2b2b2b;
    --grey-light: #e6e6e6;
    --grey-field: #e2e2e2;
    --grey-band: #c9c9c9;
    --nav-bg: rgba(45, 45, 45, 0.82);
    --serif: "EB Garamond", Georgia, serif;
    --sans: "Mulish", Helvetica, Arial, sans-serif;
  }
  * { margin: 0; padding: 0; box-sizing: border-box; }
  html, body { width: 1200px; height: 5014px; overflow: hidden; }
  body { position: relative; background: var(--white); font-family: var(--sans); color: var(--text); }
  section { position: absolute; left: 0; width: 1200px; }
  .abs { position: absolute; }
  .centered { left: 0; width: 1200px; text-align: center; }

  /* header */
  .site-header { position: absolute; top: 0; left: 0; width: 1200px; height: 100px; background: var(--nav-bg); z-index: 2; }
  .brand { position: absolute; left: 88px; top: 22px; font-family: var(--sans); font-weight: 600; font-size: 46px; color: var(--white); letter-spacing: 1px; line-height: 1; }
  .main-nav a { position: absolute; top: 44px; font-size: 15px; letter-spacing: 1.5px; color: var(--white); text-decoration: none; text-transform: uppercase; }
  .main-nav a.is-current { color: #a8a8a8; }

  /* hero */
  .hero { top: 0; height: 903px; }
  .hero-photo { position: absolute; inset: 0; background: linear-gradient(120deg, #8a8a8a 0%, #6f6f6f 35%, #4a4a4a 65%, #7b7b7b 100%); }
  .hero-title { top: 330px; font-family: var(--serif); font-size: 58px; line-height: 68px; color: var(--white); font-weight: 400; }
  .btn { display: inline-block; background: var(--purple); color: var(--white); font-size: 17px; letter-spacing: 2px; text-transform: uppercase; text-decoration: none; text-align: center; }
  .hero .btn { position: absolute; left: 471px; top: 605px; width: 257px; height: 67px; line-height: 67px; }

  .eyebrow { font-size: 17px; letter-spacing: 2px; color: var(--purple); text-transform: uppercase; }
  .rule { left: 578px; width: 44px; height: 2px; background: var(--purple); }
  .section-title { font-family: var(--serif); font-weight: 400; font-size: 56px; color: var(--black); line-height: 1.1; }
  .body-copy { font-size: 17px; line-height: 25px; color: var(--text); }

  /* about */
  .about { top: 903px; height: 852px; }
  .about .btn { position: absolute; left: 472px; top: 645px; width: 256px; height: 67px; line-height: 67px; }

  /* demo */
  .demo { top: 1755px; height: 769px; background: var(--grey-light); }

  /* purchase band */
  .purchase { top: 2524px; height: 284px; background: var(--purple); color: var(--white); }
  .purchase-title { top: 62px; font-size: 34px; font-weight: 400; }
  .purchase-sub { top: 108px; font-size: 18px; }
  .download { position: absolute; left: 486px; top: 174px; width: 224px; height: 43px; border: 2px solid var(--white); display: flex; color: var(--white); font-size: 17px; }
  .download .label { width: 150px; background: var(--white); color: var(--black); display: flex; align-items: center; gap: 14px; padding-left: 6px; }
  .download .label i { width: 38px; height: 31px; background: var(--purple); display: block; }
  .download .price { flex: 1; text-align: center; line-height: 39px; }

  /* testimonials */
  .testimonials { top: 2808px; height: 669px; }
  .quote { left: 260px; width: 680px; top: 405px; font-size: 18px; line-height: 27px; text-align: center; }
  .quote-author { left: 640px; top: 525px; font-size: 18px; }
  .arrow { top: 400px; }

  .photo-band { top: 3477px; height: 484px; background: linear-gradient(100deg, #3a3028 0%, #6c5a4e 30%, #b5aca6 60%, #d9d8dc 100%); }

  /* contact */
  .contact { top: 3961px; height: 686px; }
  .contact-form { position: absolute; left: 438px; top: 311px; width: 321px; }
  .field { display: block; width: 321px; background: var(--grey-field); border: none; font-family: var(--sans); font-size: 14px; color: #555; padding: 8px 8px; margin-bottom: 10px; height: 37px; }
  .field.message { height: 117px; margin-bottom: 6px; }
  .send { display: block; width: 321px; height: 37px; line-height: 37px; background: var(--purple); color: var(--white); font-size: 15px; letter-spacing: 2px; text-align: center; }
  .back-to-top { left: 1040px; top: 562px; width: 106px; text-align: center; font-size: 13px; letter-spacing: 1px; color: var(--black); }

  /* mailing */
  .mailing { top: 4647px; height: 367px; background: var(--grey-band); }
  .signup { position: absolute; left: 351px; top: 193px; display: flex; }
  .signup .email { width: 334px; height: 48px; background: var(--white); font-size: 14px; color: #555; padding: 0 12px; line-height: 48px; }
  .signup .subscribe { width: 165px; height: 48px; line-height: 48px; background: var(--purple); color: var(--white); font-size: 17px; letter-spacing: 2px; text-align: center; }
  .copyright { top: 326px; font-size: 12px; color: var(--text); }
</style>
</head>
<body>

<header class="site-header">
  <div class="brand">plimbo</div>
  <nav class="main-nav">
    <a class="is-current" style="left:382px">Home</a>
    <a style="left:480px">About</a>
    <a style="left:590px">Free Demo</a>
    <a style="left:720px">Testimonials</a>
    <a style="left:896px">Sleep Tips</a>
    <a style="left:1040px">Contact</a>
  </nav>
</header>

<section class="hero">
  <div class="hero-photo" role="img" aria-label="Photo of a man sleeping peacefully in bed with patterned pillows"></div>
  <h1 class="abs centered hero-title">Want to know the secret to<br>a deep and easy sleep?</h1>
  <a class="btn">Find out more</a>
</section>

<section class="about">
  <p class="abs centered eyebrow" style="top:110px">About</p>
  <div class="abs rule" style="top:143px"></div>
  <h2 class="abs centered section-title" style="top:220px">What is Plimbo?</h2>
  <p class="abs centered body-copy" style="top:338px">Plimbo is white noise that oscillates in pitch to harness the<br>calming and sedating effects of mundane repetition.</p>
  <p class="abs centered body-copy" style="top:412px">With Plimbo playing in the background,<br>we think you can expect to sleep easier and deeper.<br>We estimate you'll notice a 1 to 15% improvement<br>on how much rest you currently extract from your time in bed.</p>
  <a class="btn">Learn more</a>
</section>

<section class="demo">
  <p class="abs centered eyebrow" style="top:108px">Free Demo</p>
  <div class="abs rule" style="top:142px"></div>
  <h2 class="abs centered section-title" style="top:215px">Try it for free.</h2>
  <p class="abs centered body-copy" style="top:345px">Play this audio in the background at a low to medium decibel level<br>as you sleep. Other than the internet data used to stream, it's free.<br>Just click the play button below.</p>
  <svg class="abs" style="left:527px;top:525px" width="146" height="146" viewBox="0 0 146 146" aria-label="Play">
    <circle cx="73" cy="73" r="73" fill="var(--purple)"/>
    <path d="M66 62 L82 73 L66 84 Z" fill="#fff"/>
  </svg>
</section>

<section class="purchase">
  <p class="abs centered purchase-title">Would you like to hear more?</p>
  <p class="abs centered purchase-sub">You can purchase 10 continuous hours of audio here for only $2.99</p>
  <div class="download"><span class="label"><i></i>Download</span><span class="price">$2.99</span></div>
</section>

<section class="testimonials">
  <p class="abs centered eyebrow" style="top:125px">Testimonials</p>
  <div class="abs rule" style="top:160px"></div>
  <h2 class="abs centered section-title" style="top:222px;font-size:52px">Here's what people are saying about Plimbo.</h2>
  <svg class="abs arrow" style="left:88px" width="40" height="80" viewBox="0 0 40 80" aria-label="Previous"><path d="M36 4 L4 40 L36 76" fill="none" stroke="#111" stroke-width="3"/></svg>
  <svg class="abs arrow" style="left:1068px" width="40" height="80" viewBox="0 0 40 80" aria-label="Next"><path d="M4 4 L36 40 L4 76" fill="none" stroke="#111" stroke-width="3"/></svg>
  <p class="abs quote">"This is a testimonial where someone has written something amazing about Plimbo. They loved it and wanted to write in and say just how great it was and that they're telling all their friends."</p>
  <p class="abs quote-author">— Dorian</p>
</section>

<section class="photo-band" role="img" aria-label="Photo of a woman asleep on soft bedding, hair across the pillow"></section>

<section class="contact">
  <p class="abs centered eyebrow" style="top:85px">Contact</p>
  <div class="abs rule" style="top:120px"></div>
  <p class="abs centered body-copy" style="top:178px">Do you have any questions or comments?<br>Complete the form below and we will get back to you as soon as possible.</p>
  <div class="contact-form">
    <div class="field">Name</div>
    <div class="field">Email</div>
    <div class="field message">Message</div>
    <div class="send">SEND</div>
  </div>
  <svg class="abs" style="left:1063px;top:572px" width="60" height="60" viewBox="0 0 60 60" aria-label="Back to top">
    <circle cx="30" cy="30" r="30" fill="#111"/>
    <path d="M20 35 L30 25 L40 35" fill="none" stroke="#fff" stroke-width="2.5"/>
  </svg>
  <p class="abs back-to-top" style="top:643px">BACK TO TOP</p>
</section>

<section class="mailing">
  <p class="abs centered eyebrow" style="top:88px">Mailing List</p>
  <div class="abs rule" style="top:123px"></div>
  <div class="signup"><div class="email">Email Address</div><div class="subscribe">SUBSCRIBE</div></div>
  <p class="abs centered copyright">Copyright 2017 Plimbo. All rights reserved.</p>
</section>

</body>
</html>
```